HiItsJonBrell.com needs a modern, eye-catching business card design

My name is Jon Brell and I own a video training (software development industry) website. I need a business card design that is eye catching for when I travel to conferences or do seminars. I would prefer something simple but bold. Something along the lines of this: https://pixvaultstatic.example/gallery_img/530172/44018/44018_9917302_530172_image.jpg

Note that I do not have a specific logo, but I do have an caricature I use on my site of myself. I've not attached it because I'm not really a fan of having it on my business cards. I would prefer lettering instead of an image. You can go to my website (https://hiitsjonbrell.com) for inspiration.

I want to add the following information on my card (the order of these, their size, and their casing is up to you):

Jon Brell
jon@HiItsJonBrell.com
@HiItsJonBrell
HiItsJonBrell.com
vidsharehub.example/HiItsJonBrell

I would also like to have somewhere on the card a small ad that says "Get a free course at https://HiItsJonBrell.com/FreeCourse". Feel free to play with that wording or layout if you need. I would prefer this text to be at the bottom of the card and subtle. Some small eye-catching thing might be ok but nothing huge or garish.

I plan on printing this card at pressquill.example (https://www.pressquill.example/us/design-guidelines/business-cards.html). I would like it to be the standard size (3.66" x 2.16"). I would prefer rounded corners and horizontal orientation. This is a two-side design. I would prefer the side with all of the information be primarily white but I like color text (again, flexible on that). On the front side, I like simple. Maybe just HiItsJonBrell.com (casing on that is up to you - whatever looks and reads the best - that goes for all of the casing). As for font choices, I prefer a modern, clean font. For example, Open Sans Light can be a nice option.

Website Info (might be helpful for the card):
Color Palette

Darkest blue - #263246
Alternate blue - #2F4E6A
Light blue - #2A98C3
Orange - #FF6201
White - #FFFFFF

Font for Jon Brell Logo

Jellyka Estryas Handwriting
http://www.typecrate.example/jellyka_estryas_handwriting.font

Fonts for Site Content and VidShare Thumbnails

Lovelo (bold title font)
http://www.glyphmill.example/lovelo-font/

Open Sans (body font)
http://www.letterbarn.example/fonts/open-sans

Industry/Entity Type

Software Development

Contact Information for Business Card

Jon Brell
jon@HiItsJonBrell.com
@HiItsJonBrell
HiItsJonBrell.com
vidsharehub.example/HiItsJonBrell

Get a free course at https://HiItsJonBrell.com/FreeCourse

Colors

Designer to choose colors to be used in the design.

Requirements
Nice to have
• Modern color - maybe primarily a color on the front and then that color as an accent on the back.
Should not have
• Lots of colors - I LOVE color but do not want a rainbow of colors on the card.

```html
<!DOCTYPE html>
<html lang="en">
<head>
<meta charset="utf-8">
<title>HiItsJonBrell.com Business Card</title>
<link href="https://fonts.googleapis.com/css2?family=Montserrat:wght@300;400;500;700&display=swap" rel="stylesheet">
<style>
  :root {
    --bg-top: #161616;
    --bg-bottom: #242424;
    --card-black: #000000;
    --card-white: #ffffff;
    --ink: #111111;
    --ink-soft: #444444;
    --on-dark: #f2f2f2;
  }
  * { margin: 0; padding: 0; box-sizing: border-box; }
  html, body { width: 1200px; height: 1000px; overflow: hidden; }
  body {
    background: linear-gradient(180deg, var(--bg-top), var(--bg-bottom));
    font-family: "Montserrat", sans-serif;
    position: relative;
  }
  .card {
    position: absolute;
    left: 290px;
    width: 620px;
    height: 366px;
    border-radius: 30px;
    box-shadow: 0 14px 34px rgba(0,0,0,0.55);
  }
  .card-front {
    top: 100px;
    background: var(--card-black);
    display: flex;
    align-items: center;
    justify-content: center;
  }
  .front-domain {
    color: var(--on-dark);
    font-weight: 300;
    font-size: 34px;
    letter-spacing: 1px;
  }
  .card-back {
    top: 530px;
    background: var(--card-white);
    color: var(--ink);
  }
  .contact-row {
    position: absolute;
    top: 30px;
    left: 34px;
    right: 34px;
    display: flex;
    justify-content: space-between;
    align-items: center;
  }
  .contact {
    display: flex;
    align-items: center;
    gap: 10px;
    font-size: 13px;
    font-weight: 400;
    color: var(--ink-soft);
  }
  .contact svg { flex: none; }
  .brand {
    position: absolute;
    top: 150px;
    left: 0;
    right: 0;
    display: flex;
    justify-content: center;
    align-items: center;
    gap: 10px;
  }
  .brand-mark {
    width: 14px;
    height: 14px;
    background: var(--ink);
  }
  .brand-name {
    font-size: 34px;
    font-weight: 500;
    color: var(--ink);
    letter-spacing: 0.5px;
  }
  .promo {
    position: absolute;
    left: 40px;
    right: 40px;
    bottom: 34px;
  }
  .promo-line {
    display: flex;
    align-items: center;
    gap: 14px;
  }
  .promo-label {
    font-size: 17px;
    font-weight: 700;
    color: var(--ink);
  }
  .promo-rule {
    width: 80px;
    height: 1.5px;
    background: var(--ink);
    margin-top: 4px;
  }
  .promo-url {
    margin-top: 16px;
    text-align: right;
    font-size: 16px;
    font-weight: 400;
    color: var(--ink-soft);
  }
</style>
</head>
<body>
  <section class="card card-front" aria-label="Business card front">
    <p class="front-domain">HiItsJonBrell.com</p>
  </section>

  <section class="card card-back" aria-label="Business card back">
    <div class="contact-row">
      <div class="contact contact-email">
        <svg width="18" height="13" viewBox="0 0 18 13" aria-hidden="true">
          <rect x="0.5" y="0.5" width="17" height="12" fill="#111"/>
          <polyline points="1,1 9,7.5 17,1" fill="none" stroke="#fff" stroke-width="1.3"/>
        </svg>
        <span>jon@HiItsJonBrell.com</span>
      </div>
      <div class="contact contact-social">
        <svg width="14" height="14" viewBox="0 0 14 14" aria-hidden="true">
          <rect x="0" y="0" width="14" height="14" fill="#111"/>
        </svg>
        <span>@HiItsJonBrell</span>
      </div>
      <div class="contact contact-video">
        <svg width="14" height="14" viewBox="0 0 14 14" aria-hidden="true">
          <circle cx="7" cy="7" r="7" fill="#111"/>
        </svg>
        <span>HiItsJonBrell</span>
      </div>
    </div>

    <div class="brand">
      <span class="brand-mark" aria-hidden="true"></span>
      <span class="brand-name">Jon Brell</span>
    </div>

    <div class="promo">
      <div class="promo-line">
        <span class="promo-label">Get a FREE course at</span>
        <span class="promo-rule" aria-hidden="true"></span>
      </div>
      <p class="promo-url">https://HiItsJonBrell.com/FreeCourse</p>
    </div>
  </section>
</body>
</html>
```